Etiqueta para productos de Panaderia Albores

Necesitamos hacer una actualizacion de nuestra etiqueta con el slogan "Sabor de Siempre", les adjunto foto de la etiqueta actual y fotos de los productos en los cuales utilizamos esta etiqueta.
Somos una empresa de panaderia, ubicados en Honduras
Comercial Trigal SA de CV

Target Market(s)

Clientes en Supermercados

Industry/Entity Type

Panaderia

```html
<!DOCTYPE html>
<html lang="es">
<head>
<meta charset="utf-8">
<title>Etiqueta Panaderia Albores – Sabor de Siempre</title>
<link rel="stylesheet" href="https://fonts.googleapis.com/css2?family=Baloo+2:wght@700;800&family=Fira+Sans:ital,wght@1,700&family=Fira+Sans+Condensed:wght@400;600&display=swap">
<style>
  :root {
    --canvas: #f3f3f1;
    --navy: #0f5670;
    --navy-deep: #0b4a61;
    --gold: #f1c46e;
    --gold-soft: #f4cc80;
    --panel: #f2c97d;
    --cream: #f7efd9;
    --white: #ffffff;
  }
  html, body {
    margin: 0;
    width: 1200px;
    height: 1200px;
    overflow: hidden;
    background: var(--canvas);
  }
  .label {
    display: block;
    width: 1200px;
    height: 1200px;
  }
  .brand-name {
    font-family: "Baloo 2", sans-serif;
    font-weight: 800;
    font-size: 44px;
    letter-spacing: 9px;
    fill: var(--navy);
  }
  .slogan {
    font-family: "Baloo 2", sans-serif;
    font-weight: 700;
    font-size: 48px;
    fill: var(--gold);
  }
  .panel-title {
    font-family: "Fira Sans", sans-serif;
    font-style: italic;
    font-weight: 700;
    font-size: 19px;
    fill: var(--navy);
  }
  .panel-body {
    font-family: "Fira Sans Condensed", sans-serif;
    font-weight: 600;
    font-size: 11.2px;
    fill: var(--navy-deep);
  }
  .seal-text {
    font-family: "Fira Sans Condensed", sans-serif;
    font-weight: 600;
    font-size: 15px;
    fill: var(--white);
    letter-spacing: 0.5px;
  }
  .seal-note {
    font-family: "Fira Sans Condensed", sans-serif;
    font-weight: 400;
    font-size: 11.5px;
    fill: var(--white);
    letter-spacing: 1px;
  }
</style>
</head>
<body>
<svg class="label" viewBox="0 0 1200 1200" xmlns="http://www.w3.org/2000/svg">
  <defs>
    <path id="brand-arc" d="M 700 905 A 266 266 0 0 1 1232 905"/>
    <path id="slogan-arc" d="M 748 905 A 218 218 0 0 0 1184 905"/>
    <path id="seal-top-arc" d="M 722 1292 A 68 68 0 0 1 858 1292"/>
    <path id="seal-bottom-arc" d="M 709 1292 A 81 81 0 0 0 871 1292"/>
    <radialGradient id="portrait-tone" cx="50%" cy="45%" r="60%">
      <stop offset="0%" stop-color="#f3e2c0"/>
      <stop offset="55%" stop-color="#d9b987"/>
      <stop offset="100%" stop-color="#3aa08e"/>
    </radialGradient>
  </defs>

  <g class="label-art" transform="translate(236 75) scale(1.4) translate(-695 -640)">
    <!-- info panel -->
    <g class="info-panel">
      <rect x="722" y="1095" width="490" height="273" rx="22" fill="var(--panel)"/>
      <text class="panel-title" x="885" y="1236">LOS MEJORES INGREDIENTES</text>
      <g class="panel-body">
        <text x="885" y="1259">Lorem ipsum dolor sit amet, consectetur adipiscing elit.</text>
        <text x="885" y="1275">Pellentesque euismod lectus id augue eleifend, non blandit</text>
        <text x="890" y="1291">purus convallis. In volutpat mollis dui nec sodales. In hac</text>
        <text x="890" y="1307">habitasse platea dictumst. Donec a venenatis ante.</text>
        <text x="885" y="1323">Phasellus tempor ultrices nunc at cursus. Morbi nec lorem</text>
        <text x="885" y="1339">ullamcorper leo porttitor pretium. Suspendisse potenti.</text>
      </g>
    </g>

    <!-- brand badge -->
    <g class="brand-badge">
      <text class="brand-name" text-anchor="middle">
        <textPath href="#brand-arc" startOffset="50%">ALBORES</textPath>
      </text>
      <circle cx="780" cy="680" r="6" fill="var(--navy)"/>
      <circle cx="1152" cy="680" r="6" fill="var(--navy)"/>
      <circle cx="966" cy="905" r="250" fill="var(--navy)"/>
      <circle cx="966" cy="905" r="176" fill="var(--cream)"/>
      <circle cx="966" cy="905" r="168" fill="url(#portrait-tone)"
              role="img" aria-label="Ilustracion de una abuela panadera con delantal y rodillo"/>
      <text class="slogan" text-anchor="middle">
        <textPath href="#slogan-arc" startOffset="50%">Sabor de Siempre</textPath>
      </text>
    </g>

    <!-- artisan seal -->
    <g class="artisan-seal">
      <circle cx="790" cy="1292" r="96" fill="var(--navy)"/>
      <circle cx="790" cy="1292" r="90" fill="none" stroke="var(--white)" stroke-width="1.5" stroke-dasharray="3 4"/>
      <text class="seal-text" text-anchor="middle">
        <textPath href="#seal-top-arc" startOffset="50%">PAN ARTESANAL</textPath>
      </text>
      <text class="seal-note" text-anchor="middle">
        <textPath href="#seal-bottom-arc" startOffset="50%">RECOMENDAMOS REFRIGERAR</textPath>
      </text>
      <circle cx="790" cy="1292" r="48" fill="none" stroke="var(--white)" stroke-width="2.5"/>
      <circle cx="790" cy="1292" r="38" fill="#3d7f97"
              role="img" aria-label="Icono de espiga de trigo sobre una mano"/>
    </g>
  </g>
</svg>
</body>
</html>
```